Roofing Business needs a modern trade show booth design

Our booth is going to be a 10x10 area. we would like a back drop with two roll up banner on the sides. we would also like to have a rectangle table with our design on it.like this one https://www.flagmorrow.ca/fabric-pop-up-booth-square/p
our website is www.pelwickbuilders.ca we are updating our logo. the new one is attached. We would like one of the banners to have a vacation give away I have attached examples. Our Main Focus is roofing and eavestrough.

Target Market(s)

Home owners.

Colors

Designer to choose colors to be used in the design.

Requirements
Must have
• The same colours as my logo

```html
<!DOCTYPE html>
<html lang="en">
<head>
<meta charset="utf-8">
<title>Pelwick Roofing &amp; Eavestrough – Roll-up Banner</title>
<link rel="stylesheet" href="https://fonts.googleapis.com/css2?family=Montserrat:wght@800&family=Playfair+Display:wght@800;900&display=swap">
<style>
  :root {
    --navy: #253038;
    --orange: #f7b233;
    --orange-deep: #e8871e;
    --shadow-navy: #1f2a6b;
    --white: #ffffff;
    --strip-grey: #e6e6e6;
    --sky-top: #3f7fcf;
    --sky-mid: #8fc3ec;
    --resort: #d9c2a4;
    --pool: #36b3ea;
    --pool-deep: #1d8fd6;
    --deck: #ece6dc;
  }
  * { margin: 0; padding: 0; box-sizing: border-box; }
  html, body { width: 1200px; height: 3000px; overflow: hidden; background: var(--white); }
  .banner { position: relative; width: 1200px; height: 3000px; background: var(--white); }

  .brand {
    position: absolute; top: 0; left: 0; width: 1200px; height: 443px;
    display: flex; flex-direction: column; align-items: center; justify-content: center;
    font-family: "Montserrat", sans-serif; font-weight: 800; color: var(--navy);
  }
  .brand-mark { width: 96px; height: 96px; background: var(--orange); margin-bottom: 34px; }
  .brand-name { font-size: 104px; line-height: 1; letter-spacing: 4px; }
  .brand-tagline { font-size: 30px; letter-spacing: 5px; margin-top: 18px; }

  .hero {
    position: absolute; top: 443px; left: 0; width: 1200px; height: 1887px;
    background:
      linear-gradient(180deg,
        var(--sky-top) 0%,
        var(--sky-mid) 30%,
        #cfe6f6 38%,
        var(--resort) 46%,
        #c9a27a 52%,
        var(--deck) 57%,
        var(--pool) 62%,
        var(--pool-deep) 80%,
        var(--pool) 88%,
        var(--deck) 93%,
        var(--deck) 100%);
  }
  .headline {
    position: absolute; top: 60px; left: 0; width: 1200px; text-align: center;
    font-family: "Playfair Display", serif; font-weight: 900;
    font-size: 110px; line-height: 126px; color: var(--white);
    text-shadow: 4px 4px 0 var(--shadow-navy);
  }

  .offer {
    position: absolute; top: 2330px; left: 0; width: 1200px; height: 375px;
    background: var(--orange);
    display: flex; flex-direction: column; align-items: center; justify-content: center;
    font-family: "Playfair Display", serif; font-weight: 900; color: var(--white);
    font-size: 160px; line-height: 150px; letter-spacing: 2px;
    text-shadow: 6px 5px 0 var(--orange-deep);
  }
  .offer-strip { position: absolute; top: 2705px; left: 0; width: 1200px; height: 52px; background: var(--strip-grey); }

  .website {
    position: absolute; top: 2835px; left: 0; width: 1200px; text-align: center;
    font-family: "Montserrat", sans-serif; font-weight: 800;
    font-size: 40px; letter-spacing: 2px; color: var(--navy);
  }
</style>
</head>
<body>
  <div class="banner">
    <header class="brand">
      <div class="brand-mark"></div>
      <div class="brand-name">PELWICK</div>
      <div class="brand-tagline">ROOFING &amp; EAVESTROUGH</div>
    </header>

    <section class="hero" role="img" aria-label="Photo of a woman relaxing at the edge of a resort pool, with thatched umbrellas, loungers and a white hotel under a blue sky">
      <h1 class="headline">Book Your<br>Remodel<br>Appointment<br>Today</h1>
    </section>

    <section class="offer">
      <div>VACATION</div>
      <div>TOMORROW</div>
    </section>
    <div class="offer-strip"></div>

    <footer class="website">WWW.PELWICKBUILDERS.CA</footer>
  </div>
</body>
</html>
```